Packaging / Logo Design for Toddler Potty Liners

We need a packaging and logo design for a new company based in Atlanta called "WeeMeadow". We manufacture innovative, eco-friendly baby / toddler products. Our initial product is a flushable, biodegradable potty liner used for toddler potty training. We are looking for a modern / clean / eco-friendly packaging and logo design for this product. Each package will contain 20 liners. Box dimensions are as follows:

Length = 8.5in
Width = 5in
Height = 1.5in

The box will have a perforated top measuring 6.5 inches (see attached pictures). Liners will be folded inside and individually pulled out through the perforated top (similar to a Softrel box). See attached pictures of similar box.

Packaging should appeal to parents as an easy to use, eco-friendly, sanitary solution to potty training. This product is an alternative to the conventional way of cleaning / disinfecting the potty after each use, a process that most parents dread!

The closest competitors are NeatNips (www.neatnips-example.com) and Brillo (www.brillo-example.com) - you can reference their websites to get an idea for the product and use. However, their liners are not flushable and that is the biggest differentiator of this product. Their packaging seems conventional and non-inspiring so we would like our design to stand out from theirs.

We would like to see creative, modern cardboard box designs which will make our brand stand out from the competition. We would like to use one of the following color schemes: 1) a modern green color on a white background, 2) a modern green color on plain cardboard background, or 3) white on a modern green background. May use one or two additional complementary colors. See attached modern green image for inspiration. We would like to see clean lines, text and illustrations. We are looking forward to seeing any cool ideas you may have!
Updates

Brief has been updated with our desired color schemes and pictures for inspiration.  Please read updated brief before beginning your design!  Thanks so much!

Industry/Entity Type

Biodegradable

Requirements
Must have
• The front of the package should include the following info:

Logo: WeeMeadow
Product Name: Flushable Potty Chair Liners
Clean and Convenient
Fits All Potty Chairs
Sewer and Septic Safe
Patent Pending
20 Single-Use Flushable Potty Chair Liners

Package should also have space for some simple instructions (preferably with illustrations). This can be placed on one of the sides of the box.
1. Place liner over clean, dry (underline the word dry) potty bowl.
2. After your toddler uses the potty, remove liner (do not tie) and flush.
3. Give your toddler a high five!

Please submit design considering all sides of the box!

```html
<!DOCTYPE html>
<html lang="en">
<head>
<meta charset="utf-8">
<title>WeeMeadow Flushable Potty Chair Liners – Packaging</title>
<link href="https://fonts.googleapis.com/css2?family=Fredoka:wght@600&family=Nunito:wght@800&display=swap" rel="stylesheet">
<style>
  :root {
    --meadow-green: #80b04b;
    --paper-white: #ffffff;
    --page-bg: #ffffff;
  }
  html, body {
    margin: 0;
    padding: 0;
    width: 1200px;
    height: 1006px;
    overflow: hidden;
    background: var(--page-bg);
  }
  .canvas {
    position: relative;
    width: 1200px;
    height: 1006px;
    font-family: "Nunito", Arial, sans-serif;
    font-weight: 800;
  }

  /* Front panel */
  .front-panel {
    position: absolute;
    left: 29px;
    top: 24px;
    width: 1149px;
    height: 675px;
    background: var(--paper-white);
  }
  .top-band {
    position: absolute;
    left: 0; top: 0;
    width: 100%; height: 29px;
    background: var(--meadow-green);
  }
  .brand-lockup {
    position: absolute;
    left: 0; right: 0;
    top: 180px;
    display: flex;
    justify-content: center;
    align-items: center;
    gap: 22px;
  }
  .brand-dot {
    width: 58px;
    height: 58px;
    border-radius: 50%;
    background: var(--meadow-green);
  }
  .brand-name {
    font-family: "Fredoka", Arial, sans-serif;
    font-weight: 600;
    font-size: 112px;
    line-height: 1;
    color: var(--meadow-green);
  }
  .swoop {
    position: absolute;
    left: 0; top: 316px;
    width: 1149px; height: 150px;
  }
  .count {
    position: absolute;
    right: 20px;
    top: 412px;
    font-size: 37px;
    line-height: 1;
    color: var(--paper-white);
  }
  .product-name {
    position: absolute;
    left: 86px;
    top: 516px;
    font-family: "Fredoka", Arial, sans-serif;
    font-weight: 600;
    font-size: 73px;
    line-height: 1;
    color: var(--meadow-green);
  }
  .tagline-band {
    position: absolute;
    left: 0; top: 592px;
    width: 100%; height: 83px;
    background: var(--meadow-green);
  }
  .tagline {
    position: absolute;
    right: 96px;
    top: 610px;
    font-size: 41px;
    line-height: 1;
    color: var(--paper-white);
  }

  /* Side panel */
  .side-panel {
    position: absolute;
    left: 21px;
    top: 786px;
    width: 1150px;
    height: 203px;
    background: var(--meadow-green);
    color: var(--paper-white);
  }
  .side-title {
    position: absolute;
    left: 28px;
    top: 20px;
    margin: 0;
    font-family: "Fredoka", Arial, sans-serif;
    font-weight: 600;
    font-size: 64px;
    line-height: 60px;
  }
  .side-tagline {
    position: absolute;
    left: 30px;
    top: 148px;
    font-size: 28px;
    letter-spacing: 10px;
    line-height: 1;
  }
  .feature-box {
    position: absolute;
    left: 682px;
    top: 14px;
    width: 455px;
    height: 172px;
    box-sizing: border-box;
    border: 3px solid var(--paper-white);
    border-radius: 20px;
    margin: 0;
    padding: 8px 0 0 17px;
    list-style: none;
  }
  .feature-box li {
    font-size: 36px;
    line-height: 49px;
    white-space: nowrap;
  }
</style>
</head>
<body>
<main class="canvas">

  <section class="front-panel" aria-label="Front of box">
    <div class="top-band"></div>
    <div class="brand-lockup">
      <span class="brand-dot" aria-hidden="true"></span>
      <span class="brand-name">WeeMeadow</span>
    </div>
    <svg class="swoop" viewBox="0 0 1149 150" preserveAspectRatio="none" aria-hidden="true">
      <path d="M0 24 Q574 200 1149 24 L1149 150 L0 150 Z" fill="var(--meadow-green)"/>
    </svg>
    <div class="count">20 Liners</div>
    <div class="product-name">Flushable Potty Chair Liners</div>
    <div class="tagline-band"></div>
    <div class="tagline">Clean and Convenient</div>
  </section>

  <section class="side-panel" aria-label="Side of box">
    <h2 class="side-title">Flushable<br>Potty Chair Liners</h2>
    <div class="side-tagline">Clean and Convenient</div>
    <ul class="feature-box">
      <li>Fits All Potty Chairs</li>
      <li>Sewer and Septic Safe</li>
      <li>Patent Pending</li>
    </ul>
  </section>

</main>
</body>
</html>
```